cleaning service

we are a cleaning company,

we have a current flyer but its very dull

I have attached it, can we make it look modern, maybe add pictures and colour

```html
<!DOCTYPE html>
<html lang="en">
<head>
<meta charset="utf-8">
<title>Brightwell Cleaning Services – Trifold Brochure</title>
<link href="https://fonts.googleapis.com/css2?family=Arimo:wght@400;700&family=Open+Sans:wght@400;600;700&family=Dancing+Script:wght@700&display=swap" rel="stylesheet">
<style>
  :root{
    --teal:#4cc3cf;
    --teal-dark:#2fa9b6;
    --blue:#1f9bd9;
    --blue-deep:#1681c4;
    --heading-blue:#1b5fb4;
    --purple:#2c2088;
    --purple-deep:#1b1463;
    --ink:#3a3d44;
    --grey-box:#e4e7ea;
    --red:#c8102e;
    --gold:#f2b632;
    --page:#eef0f3;
    --white:#ffffff;
  }
  *{box-sizing:border-box;margin:0;padding:0}
  html,body{width:952px;height:1200px;overflow:hidden;background:var(--page)}
  body{font-family:"Arimo",Arial,sans-serif;color:var(--ink)}
  .canvas{position:relative;width:952px;height:1200px;overflow:hidden}

  .sheet{position:absolute;left:26px;width:900px;height:560px;display:flex;background:var(--white);box-shadow:0 6px 18px rgba(0,0,0,.18)}
  .sheet--outside{top:30px}
  .sheet--inside{top:610px}

  .panel{position:relative;width:300px;height:560px;overflow:hidden}
  .panel__backdrop{position:absolute;inset:0;width:300px;height:560px}
  .panel__copy{position:relative;padding:16px 16px 0}

  .photo{position:absolute;left:0;width:300px}

  .service{margin-bottom:10px}
  .service__head{display:flex;align-items:center;gap:8px;margin-bottom:6px}
  .service__icon{width:30px;height:30px;border-radius:4px;background:var(--teal);flex:none}
  .service__title{font-size:10.5px;color:var(--heading-blue);font-weight:400}
  .panel--dark .service__title{color:var(--teal)}
  .service__text{font-size:6.8px;line-height:1.22;text-align:justify}
  .panel--dark .service__text{color:var(--white)}
  .service__fine{font-size:5.4px;line-height:1.2;color:var(--teal-dark);margin-top:5px;text-align:justify}
  .panel--dark .service__fine{color:#7fd6f5}

  .price-table{margin-top:8px;background:var(--grey-box);border-radius:4px;overflow:hidden;font-size:6.4px}
  .price-table__head{background:var(--teal);color:var(--white);text-align:center;font-size:7px;padding:2px 0}
  .price-table__rows{padding:6px 10px 6px}
  .price-row{display:grid;grid-template-columns:122px 1fr;line-height:1.35;color:#222}
  .panel--dark .price-table{background:var(--white)}

  .note-pill{margin-top:7px;border:1px solid #c9ccd0;background:#f4f5f6;border-radius:10px;font-size:7px;padding:3px 10px;color:#222}
  .note-pill__price{color:var(--red);margin-left:4px}
  .note-pill--wide{display:flex;justify-content:space-between}

  /* About panel */
  .about__title{font-family:"Open Sans",sans-serif;font-weight:600;color:var(--white);font-size:15px;letter-spacing:.5px;margin:10px 0 10px}
  .about__text{color:var(--white);font-size:7.4px;line-height:1.24;text-align:justify;margin-bottom:9px}

  .brand-block{position:absolute;left:0;width:300px;text-align:center;color:var(--white)}
  .brand-block__title{font-family:"Open Sans",sans-serif;font-weight:600;letter-spacing:.6px}
  .brand-block__script{font-family:"Dancing Script",cursive;font-weight:700}
  .brand-block__text{font-size:8.6px;line-height:1.75;margin-top:14px;padding:0 22px}

  .call-pill{display:inline-flex;align-items:center;gap:6px;background:var(--teal);color:var(--purple-deep);border-radius:11px;padding:3px 16px;font-family:"Open Sans",sans-serif;font-weight:700;font-size:9px}
  .call-pill svg{width:9px;height:9px}
  .call-pill__number{font-size:10px}
  .call-tagline{font-family:"Open Sans",sans-serif;font-weight:700;font-size:8.5px;margin-top:6px}

  .offer-badge{position:absolute;left:196px;top:340px;width:104px;height:104px}
  .offer-badge__disc{position:absolute;inset:0;border-radius:50%;background:var(--red);border:4px solid var(--gold)}
  .offer-badge__value{position:absolute;top:17px;width:100%;text-align:center;color:var(--white);font-family:"Open Sans",sans-serif;font-weight:700;font-size:26px;line-height:1}
  .offer-badge__value small{font-size:9px}
  .offer-badge__ribbon{position:absolute;left:-22px;top:54px;width:148px;background:#a80d25;color:var(--white);text-align:center;font-family:"Open Sans",sans-serif;font-weight:700;font-size:11px;padding:3px 0;border-top:1px solid var(--gold);border-bottom:1px solid var(--gold)}

  .photo-row{display:flex;justify-content:center;gap:4px;margin:10px 0 8px}
  .photo-row__item{width:80px;height:80px;border-radius:50%;border:3px solid var(--white)}

  .inside-call{font-family:"Open Sans",sans-serif;font-weight:700;font-size:8.5px;color:#1e1e1e;display:flex;align-items:center;justify-content:center;gap:6px;margin-top:14px}
  .inside-call svg{width:9px;height:9px}
</style>
</head>
<body>
<main class="canvas">

  <!-- OUTSIDE SHEET -->
  <section class="sheet sheet--outside">

    <article class="panel panel--light">
      <div class="panel__copy">
        <div class="service">
          <div class="service__head"><span class="service__icon" role="img" aria-label="Curtain cleaning icon"></span><h3 class="service__title">Curtain Cleaning</h3></div>
          <p class="service__text">The cleaning specialists will use professional equipment and will wipe all washable surfaces down in order to eradicate and disinfect from all the harmful germs. Our broad spectrum and certified disinfectant is perfect for disease control or precautionary measure in any property or business, in order to ensure and maintain hygienic conditions. Our antiviral sanitisation service can be requested separately or combined with any of our other services.</p>
          <div class="price-table">
            <div class="price-table__head">CURTAIN CLEANING</div>
            <div class="price-table__rows">
              <div class="price-row"><span>Pair of curtains – half length</span><span>£24</span></div>
              <div class="price-row"><span>Pair of curtains – full length</span><span>£29</span></div>
            </div>
          </div>
        </div>
        <div class="service" style="margin-top:16px">
          <div class="service__head"><span class="service__icon" role="img" aria-label="Window cleaning icon"></span><h3 class="service__title">Window Cleaning</h3></div>
          <p class="service__text">Brightwell Cleaning Services offers professional window cleaning services in London. Our well-trained and vetted cleaners will do a fantastic job in keeping your property's windows bright and clean, ensuring that windows, frames and sills are cleaned professionally. You can benefit from our great expertise and affordable prices for London window cleaning.</p>
        </div>
      </div>
      <div class="photo" style="top:328px;height:232px;background:linear-gradient(160deg,#dfe6ee,#9ec6dc 55%,#5aa9cf)" role="img" aria-label="Photo of two cleaners vacuuming and wiping a bright kitchen"></div>
      <svg class="panel__backdrop" viewBox="0 0 300 560" aria-hidden="true" style="pointer-events:none">
        <path d="M0 330 Q150 300 300 340 L300 350 Q150 318 0 362 Z" fill="var(--teal)"/>
        <path d="M0 322 Q150 292 300 330 L300 340 Q150 300 0 330 Z" fill="#fff"/>
      </svg>
    </article>

    <article class="panel panel--about">
      <svg class="panel__backdrop" viewBox="0 0 300 560" aria-hidden="true">
        <defs>
          <linearGradient id="aboutBlue" x1="0" y1="0" x2="0" y2="1"><stop offset="0" stop-color="#27a9e1"/><stop offset="1" stop-color="#1583c8"/></linearGradient>
          <linearGradient id="deepPurple" x1="0" y1="0" x2="1" y2="1"><stop offset="0" stop-color="#3a2a9c"/><stop offset="1" stop-color="#1b1463"/></linearGradient>
        </defs>
        <rect width="300" height="560" fill="url(#deepPurple)"/>
        <path d="M0 0 H300 V318 Q150 362 0 338 Z" fill="url(#aboutBlue)"/>
        <path d="M0 338 Q150 362 300 318 L300 326 Q150 370 0 346 Z" fill="var(--teal)"/>
      </svg>
      <div class="panel__copy">
        <h2 class="about__title">ABOUT US</h2>
        <p class="about__text">Brightwell Cleaning Services offers professional cleaning services to make your home look its very best. From cleaning sinks, baths and tiles to polishing windows, our cleaners have the expertise to deal with every cleaning challenge.</p>
        <p class="about__text">Let me customise a cleaning service programme to suit your individual needs and your budget. Whether you require a regular service (daily, weekly or monthly) or just a one-off service, you can count on Brightwell Cleaning Services for a cleaning service at excellent rates.</p>
        <p class="about__text">In addition, Brightwell Cleaning Services believes that the products we use really matter. All the products we use are natural and non-toxic, which makes them healthier for your home and safer for the local London environment. I have personally researched all our house cleaning products to ensure they are non-toxic, biodegradable and not tested on animals.</p>
      </div>
      <div style="position:absolute;left:92px;top:298px;width:116px;height:116px;border-radius:50%;border:4px solid #fff;background:radial-gradient(circle at 50% 40%,#f2d34a,#8c8f98 55%,#5d6170)" role="img" aria-label="Photo of a vacuum cleaner on a carpet"></div>
      <div class="brand-block" style="top:428px">
        <div class="brand-block__title" style="font-size:15px">CLEANING SERVICES</div>
        <div class="brand-block__script" style="font-size:17px">by Brightwell News</div>
        <p class="brand-block__text">We can integrate the cleaning services with the newspaper delivery services and as well are offering a 20% off for all our newspaper customers and £50 for introducing us to your family and friends.</p>
      </div>
    </article>

    <article class="panel panel--cover">
      <svg class="panel__backdrop" viewBox="0 0 300 560" aria-hidden="true">
        <defs>
          <linearGradient id="coverPurple" x1="0" y1="0" x2="1" y2="1"><stop offset="0" stop-color="#3a2a9c"/><stop offset="1" stop-color="#1b1463"/></linearGradient>
        </defs>
        <rect width="300" height="560" fill="url(#coverPurple)"/>
      </svg>
      <div class="photo" style="top:0;height:380px;background:linear-gradient(180deg,#c9d8e8 0%,#a9b6c4 40%,#5f8aa8 65%,#4f8a4a 100%)" role="img" aria-label="Photo of three smiling cleaners in aprons in front of a house"></div>
      <svg class="panel__backdrop" viewBox="0 0 300 560" aria-hidden="true">
        <path d="M0 380 Q120 420 300 360 V560 H0 Z" fill="url(#coverPurple)"/>
        <path d="M0 372 Q120 412 300 352 L300 360 Q120 420 0 380 Z" fill="var(--teal)"/>
      </svg>
      <div class="offer-badge">
        <div class="offer-badge__disc"></div>
        <div class="offer-badge__value">20<small>%</small></div>
        <div class="offer-badge__ribbon">SPECIAL OFFER</div>
      </div>
      <div class="brand-block" style="top:460px">
        <div class="brand-block__title" style="font-size:19px">CLEANING SERVICES</div>
        <div class="brand-block__script" style="font-size:21px;margin-bottom:10px">by Brightwell News</div>
        <div class="call-pill">PLEASE CALL US ON
          <svg viewBox="0 0 24 24" aria-hidden="true"><path fill="currentColor" d="M6.6 10.8a15.1 15.1 0 0 0 6.6 6.6l2.2-2.2c.3-.3.7-.4 1-.2 1.1.4 2.3.6 3.6.6.6 0 1 .4 1 1V20c0 .6-.4 1-1 1C10.6 21 3 13.4 3 4c0-.6.4-1 1-1h3.5c.6 0 1 .4 1 1 0 1.3.2 2.5.6 3.6.1.3 0 .7-.2 1z"/></svg>
          <span class="call-pill__number">07700 900481</span></div>
        <div class="call-tagline">TO BEAT ANY PRICE</div>
      </div>
    </article>
  </section>

  <!-- INSIDE SHEET -->
  <section class="sheet sheet--inside">

    <article class="panel panel--light">
      <div class="photo" style="top:0;height:226px;background:linear-gradient(160deg,#d8e1ea,#b6cbe0 50%,#6ea8d4)" role="img" aria-label="Photo of a cleaner mopping beside a cleaning trolley in a kitchen"></div>
      <svg class="panel__backdrop" viewBox="0 0 300 560" aria-hidden="true">
        <path d="M0 226 Q140 196 300 206 V560 H0 Z" fill="#fff"/>
        <path d="M0 216 Q140 186 300 196 L300 206 Q140 200 0 232 Z" fill="var(--teal)"/>
      </svg>
      <div class="panel__copy" style="padding-top:244px">
        <div class="service">
          <div class="service__head"><span class="service__icon" role="img" aria-label="Sanitisation icon"></span><h3 class="service__title">Antiviral Sanitisation Service</h3></div>
          <p class="service__text">The cleaning specialists will use professional equipment and will wipe all washable surfaces down in order to eradicate and disinfect from all the harmful germs. Our broad spectrum and certified disinfectant is perfect for disease control or precautionary measure in any property or business, in order to ensure and maintain hygienic conditions. Our antiviral sanitisation service can be requested separately or combined with any of our other services.</p>
          <p class="service__fine">BS EN 1276 is the European standard for the bactericidal activity of disinfectants. Our products are tested against common germs and viruses and kill 99.999% within five minutes.</p>
          <div class="note-pill note-pill--wide"><span>Including our cleaning materials</span><span class="note-pill__price">£16 (per hour)</span></div>
        </div>
        <div class="service" style="margin-top:12px">
          <div class="service__head"><span class="service__icon" role="img" aria-label="Deep cleaning icon"></span><h3 class="service__title">One Off Deep Cleaning Service</h3></div>
          <p class="service__text">If you require one-off cleaning to freshen up your home Brightwell Cleaning Services can help you. We can arrange for a team of professional cleaners to come to your home at a time that's convenient for you. Our deep cleaning service is perfect for all households looking to save themselves from tiresome home spring cleaning.</p>
          <p class="service__fine">Our one-off service suits your home, holiday let or rental. We bring all equipment and products, work from your checklist and leave every room fresh, ready for guests or a new season.</p>
          <div class="note-pill note-pill--wide"><span>Including our cleaning materials</span><span class="note-pill__price">£16 (per hour)</span></div>
        </div>
      </div>
    </article>

    <article class="panel panel--dark">
      <svg class="panel__backdrop" viewBox="0 0 300 560" aria-hidden="true">
        <defs>
          <linearGradient id="insidePurple" x1="0" y1="0" x2="1" y2="1"><stop offset="0" stop-color="#33269a"/><stop offset="1" stop-color="#1b1463"/></linearGradient>
        </defs>
        <rect width="300" height="560" fill="url(#insidePurple)"/>
      </svg>
      <div class="panel__copy" style="padding-top:14px">
        <div class="service" style="margin-bottom:6px">
          <div class="service__head"><span class="service__icon" role="img" aria-label="Carpet cleaning icon"></span><h3 class="service__title">Carpet Cleaning</h3></div>
          <p class="service__text">Brightwell Cleaning services provides professional carpet cleaning service, carried out by our certified cleaners with years of professional experience. Our reputation speaks for itself.</p>
          <p class="service__fine">We offer deep carpet cleaning for all types of rugs and carpets, using hot water extraction to lift stains, spots and spills, with optional stain protection after every clean.</p>
          <div class="price-table">
            <div class="price-table__head">CARPET CLEANING</div>
            <div class="price-table__rows">
              <div class="price-row"><span>Single Bedroom</span><span>£19</span></div>
              <div class="price-row"><span>Double Bedroom</span><span>£24</span></div>
              <div class="price-row"><span>Living / Dining / Lounge</span><span>£29</span></div>
              <div class="price-row"><span>Hallway</span><span>£13</span></div>
              <div class="price-row"><span>Landing</span><span>£7</span></div>
              <div class="price-row"><span>Steps</span><span>£2 &nbsp;( per step )</span></div>
              <div class="price-row"><span>Bathroom</span><span>£6</span></div>
            </div>
          </div>
          <div class="note-pill">Including our cleaning materials<span class="note-pill__price">Minimum charge of £49</span></div>
        </div>
        <div class="photo-row">
          <div class="photo-row__item" style="background:radial-gradient(circle,#f3dc5a,#9fc6e4)" role="img" aria-label="Photo of a gloved hand spraying a window"></div>
          <div class="photo-row__item" style="background:radial-gradient(circle,#d9d2c4,#8aa0a8)" role="img" aria-label="Photo of a rug being steam cleaned"></div>
          <div class="photo-row__item" style="background:radial-gradient(circle,#f2c94c,#c9a77a)" role="img" aria-label="Photo of a hand wiping a wooden table"></div>
        </div>
        <div class="service" style="margin-bottom:6px">
          <div class="service__head"><span class="service__icon" role="img" aria-label="Rug cleaning icon"></span><h3 class="service__title">Rug Cleaning</h3></div>
          <p class="service__text">Brightwell Cleaning services offers professional rug cleaning service at competitive prices! Book our skilled technicians and have your textile floorings impeccably cleaned in no time. We will bring the as-new look of any rug, including antique rugs, Persian rugs, area rugs and more. If you need us to deal with a nasty stain or any other accident on your rug, you can now book our emergency rug cleaning service for a same-day appointment at no extra cost!</p>
        </div>
        <div class="service">
          <div class="service__head"><span class="service__icon" role="img" aria-label="Oven cleaning icon"></span><h3 class="service__title">Oven Cleaning From £42</h3></div>
          <p class="service__text">Brightwell Cleaning services offers professional oven cleaning service at competitive prices! Book our skilled technicians and have your oven impeccably cleaned in no time. We will bring the as-new look of any oven, including range cookers, hobs, grills and more. If you need us to deal with a nasty spill or any other accident in your oven, you can now book our emergency cleaning service for a same-day appointment at no extra cost!</p>
          <p class="service__fine">We provide professional oven cleaning across London. We remove grease and burnt food from hobs, racks and burners, then clean the appliance inside and out, including the door.</p>
        </div>
      </div>
    </article>

    <article class="panel panel--light">
      <div class="panel__copy" style="padding-top:16px">
        <div class="service">
          <div class="service__head"><span class="service__icon" role="img" aria-label="Upholstery cleaning icon"></span><h3 class="service__title">Upholstery Cleaning</h3></div>
          <p class="service__text">Keeping your home clean is vital and taking care of upholstery is an important part of that. If you're struggling to find time around the demands of family and/or career, Brightwell Cleaning can help.</p>
          <div class="price-table">
            <div class="price-table__head">UPHOLSTERY CLEANING</div>
            <div class="price-table__rows">
              <div class="price-row"><span>Armchair</span><span>£17</span></div>
              <div class="price-row"><span>Two seater sofa</span><span>£22</span></div>
              <div class="price-row"><span>Three seater sofa</span><span>£32</span></div>
              <div class="price-row"><span>Four seater sofa</span><span>£42</span></div>
              <div class="price-row"><span>Dining chair</span><span>£5</span></div>
            </div>
          </div>
          <p class="service__fine">Our upholstery team cleans sofas, armchairs, dining chairs and ottomans. We treat natural and synthetic fabrics, from leather, wool and suede to microfibre and faux fur, with care.</p>
          <div class="note-pill">Including our cleaning materials<span class="note-pill__price">Minimum charge of £49</span></div>
        </div>
        <div class="service" style="margin-top:14px">
          <div class="service__head"><span class="service__icon" role="img" aria-label="Mattress cleaning icon"></span><h3 class="service__title">Mattress Cleaning</h3></div>
          <p class="service__text">Brightwell Cleaning Services provides mattress cleaning for your residential property in. Our technicians use safe but efficient solutions and powerful professional equipment to remove dirt, dust, and bacteria from your bedding. We can deal with all kinds of stains on your mattress and will restore its as-new look at an inexpensive price.</p>
          <div class="price-table">
            <div class="price-table__head">MATTRESS CLEANING</div>
            <div class="price-table__rows">
              <div class="price-row"><span>Single Mattress both sides</span><span>£19</span></div>
              <div class="price-row"><span>Double Mattress both sides</span><span>£29</span></div>
            </div>
          </div>
        </div>
        <div class="inside-call">PLEASE CALL US ON
          <svg viewBox="0 0 24 24" aria-hidden="true"><path fill="currentColor" d="M6.6 10.8a15.1 15.1 0 0 0 6.6 6.6l2.2-2.2c.3-.3.7-.4 1-.2 1.1.4 2.3.6 3.6.6.6 0 1 .4 1 1V20c0 .6-.4 1-1 1C10.6 21 3 13.4 3 4c0-.6.4-1 1-1h3.5c.6 0 1 .4 1 1 0 1.3.2 2.5.6 3.6.1.3 0 .7-.2 1z"/></svg>
          07700 900481</div>
      </div>
      <div class="photo" style="top:380px;height:180px;background:linear-gradient(160deg,#eef0f2,#cfd6dc 55%,#8f9aa6)" role="img" aria-label="Photo of a cleaner vacuuming a living room floor"></div>
      <svg class="panel__backdrop" viewBox="0 0 300 560" aria-hidden="true" style="pointer-events:none">
        <path d="M0 380 H300 V360 Q160 440 0 404 Z" fill="#fff"/>
        <path d="M0 404 Q160 440 300 360 L300 372 Q160 452 0 416 Z" fill="var(--teal)"/>
      </svg>
    </article>
  </section>

</main>
</body>
</html>
```